Kelvora

I ran out of business cards I designed myself on line. THe company went out of business and I LOVE my card. I am hoping someone can recreate the look or something equally as appealing to me.

Industry/Entity Type

Business

Colors
ecdaeb
f7f1f7

Requirements
Must have
• The card is going to be printed by a company Taroq.com. they are very high end stock and I market to high end clients…the logo needs to remain small and centered at the top. If it helps my web site is kelvora.net you can see there how I left the logo very small

```html
<!DOCTYPE html>
<html lang="en">
<head>
<meta charset="utf-8">
<title>Kelvora, LLC — Business Card</title>
<link href="https://fonts.googleapis.com/css2?family=EB+Garamond:wght@600&display=swap" rel="stylesheet">
<style>
  :root {
    --backdrop: #e6e7e8;
    --card-border: #ecdaeb;
    --card-face: #f7f1f7;
    --ink-bronze: #b08358;
    --card-shadow: rgba(60, 60, 70, 0.55);
  }
  * { margin: 0; padding: 0; box-sizing: border-box; }
  html, body {
    width: 1200px;
    height: 1000px;
    overflow: hidden;
    background: var(--backdrop);
  }
  .canvas {
    position: relative;
    width: 1200px;
    height: 1000px;
  }
  .business-card {
    position: absolute;
    left: 357px;
    top: 128px;
    width: 486px;
    height: 743px;
    background: var(--card-border);
    box-shadow: 4px 4px 5px var(--card-shadow);
  }
  .card-face {
    position: absolute;
    left: 17px;
    top: 18px;
    right: 17px;
    bottom: 18px;
    background: var(--card-face);
  }
  .card-text {
    position: absolute;
    left: 0;
    width: 100%;
    text-align: center;
    font-family: "EB Garamond", "Times New Roman", serif;
    font-weight: 600;
    color: var(--ink-bronze);
    text-transform: uppercase;
    white-space: nowrap;
  }
  .brand-mark {
    top: 138px;
    font-size: 30px;
    letter-spacing: 4px;
  }
  .company-name {
    top: 256px;
    font-size: 45px;
    letter-spacing: 0.5px;
  }
  .services {
    top: 404px;
    font-size: 28px;
    letter-spacing: 0.5px;
  }
  .contact {
    top: 536px;
    font-size: 26px;
    line-height: 40px;
    letter-spacing: 0.3px;
  }
</style>
</head>
<body>
  <main class="canvas">
    <article class="business-card">
      <div class="card-face">
        <div class="card-text brand-mark">Kelvora</div>
        <h1 class="card-text company-name">Kelvora, LLC</h1>
        <p class="card-text services">Design &amp; Renovation</p>
        <address class="card-text contact" style="font-style: normal;">
          Maren Ostrow<br>
          410-555-0187<br>
          maren@kelvora.net
        </address>
      </div>
    </article>
  </main>
</body>
</html>
```